Stationery for Villa Marejada Design Hotel**

Who we are:

Wander on an isolated beach while breathing in the fresh, salty, sea air. Listen to the warm Pacific wind rustling through green palm trees as you walk to a pristine lagoon. Feel the delicious warmth of the sun kiss your skin; the beach is yours. At Villa Marejada you can experience a vacation in undisturbed, natural beauty. We have created a place for you to find new strength, relaxation, and inner harmony. We offer total rest to the experienced traveler from all over the world.

We are a brand new and smartly built design-hotel (under construction) close to a unique beach and a fantastic surf spot in Huatulco, Southwest Mexico.

As you can see in the attachments, we do have an established corporate design, but as for now still need a format for booklets for information around our hotel and things to do in the area, important numbers (we fill in the content for that one).

Our corporate colors:
green #64b445, brown #b07043, blue #0ab7cf, yellow # f9b02a and #fcc01a, navy #444f69
Corporate fonts:
Krub and Miller Banner.
For further information access:
www.villamarejada.example
https://slideshare.example/view/QxLmPwTr8KdNvYsZhJcA/

Social Media: VillaMarejada

Industry/Entity Type

Hotel

Font styles to use
Other font styles liked:
• Krub, Miller Banner

Requirements
Must have
• Stick to Logo Design, defined corporate elements, logo, colors, fonts and general touch and feel
Nice to have
• Who we are:

Our corporate colors:
Corporate fonts:
Krub and Miller Banner.
www.villamarejada.example

Social Media: VillaMarejada

```html
<!DOCTYPE html>
<html lang="en">
<head>
<meta charset="utf-8">
<title>Villa Marejada – Business Card</title>
<link href="https://fonts.googleapis.com/css2?family=Krub:wght@400;500;600&family=Source+Serif+4:opsz,wght@8..60,700&display=swap" rel="stylesheet">
<style>
  :root {
    --backdrop: #0f3a3a;
    --navy: #4a5273;
    --navy-text: #444f69;
    --paper: #f4f4f2;
    --green: #64b445;
    --gold: #e2b52a;
  }
  * { margin: 0; padding: 0; box-sizing: border-box; }
  html, body { width: 1200px; height: 1189px; overflow: hidden; }
  body {
    background: var(--backdrop);
    font-family: "Krub", sans-serif;
    position: relative;
  }
  .card {
    position: absolute;
    left: 326px;
    width: 576px;
    height: 329px;
  }
  .card-front {
    top: 215px;
    background: var(--navy);
    display: flex;
    flex-direction: column;
    align-items: center;
    justify-content: center;
    gap: 18px;
  }
  .brand-mark {
    display: block;
    border: 3px solid var(--gold);
  }
  .card-front .brand-mark { width: 46px; height: 46px; }
  .brand-name {
    font-family: "Krub", sans-serif;
    font-weight: 600;
    color: var(--gold);
    letter-spacing: 0.04em;
    text-transform: uppercase;
  }
  .card-front .brand-name { font-size: 30px; }

  .card-back {
    top: 645px;
    background: linear-gradient(135deg, #ffffff 0%, var(--paper) 60%, #e9e9e7 100%);
    color: var(--navy-text);
  }
  .contact {
    position: absolute;
    left: 55px;
    top: 42px;
  }
  .person-name {
    font-family: "Source Serif 4", serif;
    font-weight: 700;
    font-size: 22px;
    color: var(--green);
    line-height: 1.1;
  }
  .person-role { font-size: 15px; line-height: 1.2; }
  .address {
    margin-top: 52px;
    font-style: normal;
    font-size: 14.5px;
    line-height: 18px;
  }
  .lines { margin-top: 14px; font-size: 14.5px; line-height: 20px; }
  .lines .label { color: var(--green); font-weight: 500; }
  .web { margin-top: 13px; font-size: 14.5px; }
  .back-brand {
    position: absolute;
    right: 50px;
    bottom: 52px;
    display: flex;
    flex-direction: column;
    align-items: center;
    gap: 10px;
  }
  .back-brand .brand-mark { width: 28px; height: 28px; border-width: 2px; }
  .back-brand .brand-name { font-size: 15px; }
</style>
</head>
<body>
  <section class="card card-front">
    <span class="brand-mark"></span>
    <span class="brand-name">Villa Marejada</span>
  </section>

  <section class="card card-back">
    <div class="contact">
      <h1 class="person-name">Lucia Ferrand</h1>
      <p class="person-role">Founder</p>
      <address class="address">
        Villa Marejada<br>
        Punta Marejada, Huatulco<br>
        Oaxaca, Mexiko
      </address>
      <p class="lines">
        <span class="label">T :</span> +52 1 (958) 555 0142<br>
        <span class="label">E :</span> hello@villamarejada.example
      </p>
      <p class="web">www.villamarejada.example</p>
    </div>
    <div class="back-brand">
      <span class="brand-mark"></span>
      <span class="brand-name">Villa Marejada</span>
    </div>
  </section>
</body>
</html>
```